MTSS Pyramid graphic needed for use in presentations and on my website

I am a consultant and need graphics to represent the MTSS pyramid (educational terminology) for use on my website and in slide decks. I've included documentation below that shows the MTSS pyramid, some preferences I have thought of, and my color palette. The MTSS pyramid is well-known in my field and I'd like one that I can use in all my presentations and on my website that looks professional and modern.

Target Market(s)

Educational leaders and educators

Industry/Entity Type

Educational Consulting

Font styles to use
Serif
Sans Serif

Colors
00AB8E
00BBA5
67D7C9
C6EFE9
E9F9F6
6B429C
8869AF
B7A5CE
E3DAEB
F3F0F8

Requirements
Must have
• a pyramid that can be recognized as an MTSS pyramid, use of colors that align with my color palette, a professional, modern look and feel, 3 sections with the largest at the bottom of the pyramid
Nice to have
• rounded corners, maybe 3D
Should not have
• a pyramid in a different shape or orientation, any more or fewer than 3 sections

```html
<!DOCTYPE html>
<html lang="en">
<head>
<meta charset="utf-8">
<title>MTSS Pyramid Tier Set</title>
<link rel="stylesheet" href="https://fonts.googleapis.com/css2?family=Roboto:wght@400;700&display=swap">
<style>
  :root {
    --page: #ffffff;
    --tier3-dark: #3f4152;
    --tier3-light: #5b5d70;
    --tier2-dark: #456582;
    --tier2-light: #5d7f9c;
    --tier1-dark: #4f9896;
    --tier1-light: #78b7ad;
    --muted-dark: #cfcfcf;
    --muted-light: #e6e6e6;
    --divider: rgba(255,255,255,0.75);
    --label-on: #ffffff;
    --label-off: #9d9d9d;
  }
  html, body {
    margin: 0;
    padding: 0;
    width: 1200px;
    height: 2572px;
    overflow: hidden;
    background: var(--page);
  }
  .pyramid-sheet { display: block; width: 1200px; height: 2572px; }
  .tier-label {
    font-family: "Roboto", Arial, sans-serif;
    font-size: 22px;
    text-anchor: middle;
  }
  .tier-label .tier-number { font-weight: 700; }
  .tier-label.is-active { fill: var(--label-on); }
  .tier-label.is-muted { fill: var(--label-off); }
  .tier-divider { stroke: var(--divider); stroke-width: 2; }
  .stop-t3a { stop-color: var(--tier3-light); } .stop-t3b { stop-color: var(--tier3-dark); }
  .stop-t2a { stop-color: var(--tier2-light); } .stop-t2b { stop-color: var(--tier2-dark); }
  .stop-t1a { stop-color: var(--tier1-light); } .stop-t1b { stop-color: var(--tier1-dark); }
  .stop-mua { stop-color: var(--muted-light); } .stop-mub { stop-color: var(--muted-dark); }
</style>
</head>
<body>
<svg class="pyramid-sheet" viewBox="0 0 1200 2572" xmlns="http://www.w3.org/2000/svg" role="img" aria-label="MTSS pyramid in five tier-highlight variations, labelled and unlabelled">
  <defs>
    <clipPath id="pyramid-outline" clipPathUnits="userSpaceOnUse">
      <path d="M196 18 Q230 -10 264 18 L452 336 Q474 380 428 402 Q230 420 32 402 Q-14 380 8 336 Z"/>
    </clipPath>
    <radialGradient id="fill-tier3" cx="0.5" cy="0.6" r="0.7"><stop offset="0" class="stop-t3a"/><stop offset="1" class="stop-t3b"/></radialGradient>
    <radialGradient id="fill-tier2" cx="0.5" cy="0.6" r="0.7"><stop offset="0" class="stop-t2a"/><stop offset="1" class="stop-t2b"/></radialGradient>
    <radialGradient id="fill-tier1" cx="0.5" cy="0.5" r="0.7"><stop offset="0" class="stop-t1a"/><stop offset="1" class="stop-t1b"/></radialGradient>
    <radialGradient id="fill-muted" cx="0.5" cy="0.5" r="0.7"><stop offset="0" class="stop-mua"/><stop offset="1" class="stop-mub"/></radialGradient>

    <g id="labels-all">
      <text class="tier-label is-active"><tspan class="tier-number" x="230" y="66">Tier 3</tspan><tspan x="230" y="92">Intensive</tspan><tspan x="230" y="118">Intervention</tspan></text>
      <text class="tier-label is-active"><tspan class="tier-number" x="230" y="186">Tier 2</tspan><tspan x="230" y="212">Targeted</tspan><tspan x="230" y="238">Intervention</tspan></text>
      <text class="tier-label is-active"><tspan class="tier-number" x="230" y="326">Tier 1</tspan><tspan x="230" y="352">Core Instruction</tspan></text>
    </g>
  </defs>

  <!-- Row 1: all tiers -->
  <g transform="translate(100 88)" clip-path="url(#pyramid-outline)">
    <rect width="460" height="132" fill="url(#fill-tier3)"/>
    <rect y="132" width="460" height="132" fill="url(#fill-tier2)"/>
    <rect y="264" width="460" height="160" fill="url(#fill-tier1)"/>
    <line class="tier-divider" x1="0" y1="132" x2="460" y2="132"/><line class="tier-divider" x1="0" y1="264" x2="460" y2="264"/>
    <use href="#labels-all"/>
  </g>
  <g transform="translate(616 88)" clip-path="url(#pyramid-outline)">
    <rect width="460" height="132" fill="url(#fill-tier3)"/>
    <rect y="132" width="460" height="132" fill="url(#fill-tier2)"/>
    <rect y="264" width="460" height="160" fill="url(#fill-tier1)"/>
    <line class="tier-divider" x1="0" y1="132" x2="460" y2="132"/><line class="tier-divider" x1="0" y1="264" x2="460" y2="264"/>
  </g>

  <!-- Row 2: tier 1 highlighted -->
  <g transform="translate(100 576)" clip-path="url(#pyramid-outline)">
    <rect width="460" height="264" fill="url(#fill-muted)"/>
    <rect y="264" width="460" height="160" fill="url(#fill-tier1)"/>
    <line class="tier-divider" x1="0" y1="132" x2="460" y2="132"/><line class="tier-divider" x1="0" y1="264" x2="460" y2="264"/>
    <text class="tier-label is-muted"><tspan class="tier-number" x="230" y="66">Tier 3</tspan><tspan x="230" y="92">Intensive</tspan><tspan x="230" y="118">Intervention</tspan></text>
    <text class="tier-label is-muted"><tspan class="tier-number" x="230" y="186">Tier 2</tspan><tspan x="230" y="212">Targeted</tspan><tspan x="230" y="238">Intervention</tspan></text>
    <text class="tier-label is-active"><tspan class="tier-number" x="230" y="326">Tier 1</tspan><tspan x="230" y="352">Core Instruction</tspan></text>
  </g>
  <g transform="translate(616 576)" clip-path="url(#pyramid-outline)">
    <rect width="460" height="264" fill="url(#fill-muted)"/>
    <rect y="264" width="460" height="160" fill="url(#fill-tier1)"/>
    <line class="tier-divider" x1="0" y1="132" x2="460" y2="132"/><line class="tier-divider" x1="0" y1="264" x2="460" y2="264"/>
  </g>

  <!-- Row 3: tier 2 highlighted -->
  <g transform="translate(100 1064)" clip-path="url(#pyramid-outline)">
    <rect width="460" height="132" fill="url(#fill-muted)"/>
    <rect y="132" width="460" height="132" fill="url(#fill-tier2)"/>
    <rect y="264" width="460" height="160" fill="url(#fill-muted)"/>
    <line class="tier-divider" x1="0" y1="132" x2="460" y2="132"/><line class="tier-divider" x1="0" y1="264" x2="460" y2="264"/>
    <text class="tier-label is-muted"><tspan class="tier-number" x="230" y="66">Tier 3</tspan><tspan x="230" y="92">Intensive</tspan><tspan x="230" y="118">Intervention</tspan></text>
    <text class="tier-label is-active"><tspan class="tier-number" x="230" y="186">Tier 2</tspan><tspan x="230" y="212">Targeted</tspan><tspan x="230" y="238">Intervention</tspan></text>
    <text class="tier-label is-muted"><tspan class="tier-number" x="230" y="326">Tier 1</tspan><tspan x="230" y="352">Core Instruction</tspan></text>
  </g>
  <g transform="translate(616 1064)" clip-path="url(#pyramid-outline)">
    <rect width="460" height="132" fill="url(#fill-muted)"/>
    <rect y="132" width="460" height="132" fill="url(#fill-tier2)"/>
    <rect y="264" width="460" height="160" fill="url(#fill-muted)"/>
    <line class="tier-divider" x1="0" y1="132" x2="460" y2="132"/><line class="tier-divider" x1="0" y1="264" x2="460" y2="264"/>
  </g>

  <!-- Row 4: tier 3 highlighted -->
  <g transform="translate(100 1552)" clip-path="url(#pyramid-outline)">
    <rect width="460" height="132" fill="url(#fill-tier3)"/>
    <rect y="132" width="460" height="292" fill="url(#fill-muted)"/>
    <line class="tier-divider" x1="0" y1="132" x2="460" y2="132"/><line class="tier-divider" x1="0" y1="264" x2="460" y2="264"/>
    <text class="tier-label is-active"><tspan class="tier-number" x="230" y="66">Tier 3</tspan><tspan x="230" y="92">Intensive</tspan><tspan x="230" y="118">Intervention</tspan></text>
    <text class="tier-label is-muted"><tspan class="tier-number" x="230" y="186">Tier 2</tspan><tspan x="230" y="212">Targeted</tspan><tspan x="230" y="238">Intervention</tspan></text>
    <text class="tier-label is-muted"><tspan class="tier-number" x="230" y="326">Tier 1</tspan><tspan x="230" y="352">Core Instruction</tspan></text>
  </g>
  <g transform="translate(616 1552)" clip-path="url(#pyramid-outline)">
    <rect width="460" height="132" fill="url(#fill-tier3)"/>
    <rect y="132" width="460" height="292" fill="url(#fill-muted)"/>
    <line class="tier-divider" x1="0" y1="132" x2="460" y2="132"/><line class="tier-divider" x1="0" y1="264" x2="460" y2="264"/>
  </g>

  <!-- Row 5: tiers 1 and 2 highlighted -->
  <g transform="translate(100 2040)" clip-path="url(#pyramid-outline)">
    <rect width="460" height="132" fill="url(#fill-muted)"/>
    <rect y="132" width="460" height="132" fill="url(#fill-tier2)"/>
    <rect y="264" width="460" height="160" fill="url(#fill-tier1)"/>
    <line class="tier-divider" x1="0" y1="132" x2="460" y2="132"/><line class="tier-divider" x1="0" y1="264" x2="460" y2="264"/>
    <text class="tier-label is-muted"><tspan class="tier-number" x="230" y="66">Tier 3</tspan><tspan x="230" y="92">Intensive</tspan><tspan x="230" y="118">Intervention</tspan></text>
    <text class="tier-label is-active"><tspan class="tier-number" x="230" y="186">Tier 2</tspan><tspan x="230" y="212">Targeted</tspan><tspan x="230" y="238">Intervention</tspan></text>
    <text class="tier-label is-active"><tspan class="tier-number" x="230" y="326">Tier 1</tspan><tspan x="230" y="352">Core Instruction</tspan></text>
  </g>
  <g transform="translate(616 2040)" clip-path="url(#pyramid-outline)">
    <rect width="460" height="132" fill="url(#fill-muted)"/>
    <rect y="132" width="460" height="132" fill="url(#fill-tier2)"/>
    <rect y="264" width="460" height="160" fill="url(#fill-tier1)"/>
    <line class="tier-divider" x1="0" y1="132" x2="460" y2="132"/><line class="tier-divider" x1="0" y1="264" x2="460" y2="264"/>
  </g>
</svg>
</body>
</html>
```